Business Card for Consulting Company

I would need a business card for my consulting company - the company brand and logos are defined and shared as part of this project. The proposed design for the business card can be reused as inspiration for my email signature.

```html
<!DOCTYPE html>
<html lang="en">
<head>
<meta charset="utf-8">
<title>Northvale – Business Card</title>
<link rel="stylesheet" href="https://fonts.googleapis.com/css2?family=Exo+2:wght@500&family=Open+Sans:wght@400&display=swap">
<style>
  :root {
    --backdrop: #1c1c1c;
    --card: #3d3d3d;
    --teal: #009ca6;
    --white: #ffffff;
  }
  * { margin: 0; padding: 0; box-sizing: border-box; }
  html, body { width: 1200px; height: 895px; overflow: hidden; }
  body {
    background: var(--backdrop);
    display: flex;
    align-items: center;
    justify-content: center;
    gap: 40px;
  }
  .card {
    width: 540px;
    height: 318px;
    background: var(--card);
    position: relative;
    overflow: hidden;
    box-shadow: 0 10px 30px rgba(0,0,0,0.5);
  }
  .card-front {
    display: flex;
    align-items: center;
    justify-content: center;
  }
  .brand {
    display: flex;
    align-items: center;
    gap: 12px;
  }
  .brand-dot {
    width: 22px;
    height: 22px;
    border-radius: 50%;
    background: var(--teal);
  }
  .brand-name {
    font-family: "Exo 2", sans-serif;
    font-weight: 500;
    font-size: 40px;
    letter-spacing: 1px;
    color: var(--white);
  }
  .accent-disc {
    position: absolute;
    right: -70px;
    top: 30px;
    width: 300px;
    height: 300px;
    border-radius: 50%;
    background: var(--teal);
  }
  .card-back .contact-block {
    position: absolute;
    left: 40px;
    bottom: 34px;
    color: var(--white);
  }
  .person-name {
    font-family: "Exo 2", sans-serif;
    font-weight: 500;
    font-size: 30px;
    color: var(--teal);
    line-height: 1.1;
  }
  .person-title {
    font-family: "Open Sans", sans-serif;
    font-size: 14px;
    margin-top: 2px;
  }
  .contact-list {
    list-style: none;
    margin-top: 22px;
    font-family: "Open Sans", sans-serif;
    font-size: 14px;
    line-height: 1.5;
  }
</style>
</head>
<body>
  <section class="card card-front">
    <div class="brand">
      <span class="brand-dot"></span>
      <span class="brand-name">Northvale</span>
    </div>
  </section>

  <section class="card card-back">
    <span class="accent-disc"></span>
    <div class="contact-block">
      <h1 class="person-name">Elise Marchand</h1>
      <p class="person-title">Founder &amp; CEO</p>
      <ul class="contact-list">
        <li>+41 79 555 01 23</li>
        <li>elise.m@northvale.ch</li>
        <li>www.northvale.ch</li>
      </ul>
    </div>
  </section>
</body>
</html>
```